Verpackungsdesign für Räucherstäbchen
Zielgruppe
Unsere Firma Lindenkram importiert hochwertige und reine Räucherstoffe aus entfernten Ländern. Dabei steht die Nachhaltigkeit und der faire Handel im Vordergrund. Unser Fokus ist dabei der Handel mit Weihrauch, den wir aus den Ursprungsländern importieren und an Großhändler, Händler und Endkunden weiterverkaufen. Seit einigen Jahren haben wir den Wunsch echte, natürliche Räucherstäbchen auf den Markt zu bringen. Dieses Projekt wurde nun umgesetzt.
Wir suchen ein Verpackungsdesign für unsere Räucherstäbchen. Die Räucherstäbchen sind absolut naturrein (95% aller Räucherstäbchen auf dem Markt sind es nicht), ohne Chemie, ohne Parfum, ohne Synthetik. Absolut rein, hergestellt aus besten Rohstoffen, teilweise direkt aus Deutschland.
Aufgabenstellung
Da die Räucherstäbchen auch in den Handel kommen werden, ist es am Besten, dass die Verpackung eine Faltschachtel ist mit den Maßen: 6cm Breite, 22cm Länge, 1,5cm Höhe
Die Schachtel sollte sehr natürlich ausschauen und die Farben nicht zu kräftig.
Es wird ein Logo darauf geben, das ich hochladen werde.
Farben sollten natürlich sein, Elegant und natürlich. Wir wissen nicht genau, wie die Verpackung aussehen soll, doch sicher ist, dass sie nicht zu überladen sein sollte. Die Verpackung sollte schlicht, natürlich und edel sein
Wir planen über 20 Sorten: Harze, Sandelholz, Patchouli etc.
Das Design der Verpackung sollte das berücksichtigen. Ein Design, das später an die verschiedenen Sorten angepasst werden kann
Für das Beispiel-Design:
Text auf der Vorderseite:
Räucherstäbchen
Weihrauch Afrika
Made with love in Germany
Natur pur
Rückseite:
Naturreine Räucherstäbchen hergestellt mit den reinsten Rohstoffen
Ohne chemische oder synthetische Zusätze, kein Parfum, keine Abbrennhilfe
Brenndauer: ca. 45- 60min
Eine Verpackung beinhaltet 10 Räucherstäbchen.
Hergestellt von:
Made by
Lindenkram
Birkenauer Weg 14
35127 Lindental

```html
<!DOCTYPE html>
<html lang="de">
<head>
<meta charset="utf-8">
<title>Lindenkram – Räucherstäbchen Weihrauch Afrika</title>
<link href="https://fonts.googleapis.com/css2?family=Bebas+Neue&family=Jost:wght@300;400&display=swap" rel="stylesheet">
<style>
  :root {
    --paper: #ffffff;
    --panel: #f4efe9;
    --panel-edge: #cfcac6;
    --spine: #a58b7a;
    --band: #8f7567;
    --band-dark: #5a463b;
    --taupe: #a48b7a;
    --green: #5e8a5c;
    --green-dark: #4f7a52;
    --address: #7f7a5e;
    --lettering: #dfe3d6;
    --white: #ffffff;
  }
  * { margin: 0; padding: 0; box-sizing: border-box; }
  html, body { width: 849px; height: 1200px; overflow: hidden; background: var(--paper); }
  .canvas { position: relative; width: 849px; height: 1200px; font-family: "Jost", sans-serif; }

  .panel { position: absolute; top: 129px; height: 891px; background: var(--panel); border: 1px solid var(--panel-edge); }
  .panel--front { left: 160px; width: 243px; }
  .panel--back { left: 464px; width: 244px; }
  .spine { position: absolute; top: 129px; left: 403px; width: 61px; height: 891px; background: var(--spine); }

  .brand-mark { position: absolute; left: 208px; top: 209px; width: 146px; height: 146px;
    border: 1px solid var(--green); border-radius: 50%;
    display: flex; align-items: center; justify-content: center; }
  .brand-mark__name { font-weight: 300; font-size: 20px; color: var(--green); letter-spacing: 0.04em; }

  .category, .claim { position: absolute; left: 160px; width: 243px; text-align: center;
    color: var(--taupe); font-weight: 400; font-size: 15.5px; line-height: 1; }
  .category { top: 556px; letter-spacing: 0.235em; padding-left: 0.235em; }
  .claim { top: 846px; letter-spacing: 0.26em; padding-left: 0.26em; }

  .band { position: absolute; overflow: hidden; }
  .band__pattern { position: absolute; inset: 0; background: linear-gradient(180deg, var(--band) 0%, var(--band-dark) 50%, var(--band) 100%); }
  .band--front { left: 160px; top: 590px; width: 244px; height: 232px; }
  .band--back { left: 464px; top: 248px; width: 241px; height: 93px; }
  .band__title { position: absolute; inset: 0; display: flex; flex-direction: column; align-items: center; justify-content: center;
    font-family: "Bebas Neue", sans-serif; font-weight: 400; color: var(--white); letter-spacing: 0.09em; line-height: 0.93; text-align: center; }
  .band--front .band__title { font-size: 44px; }
  .band--back .band__title { font-size: 31px; }

  .count { position: absolute; left: 160px; top: 944px; width: 48px; height: 29px; background: var(--green-dark);
    color: var(--white); font-size: 14px; display: flex; align-items: center; justify-content: center; }
  .lettering { position: absolute; left: 226px; top: 949px; width: 120px; height: 20px; background: var(--lettering); border-radius: 3px; }

  .copy { position: absolute; left: 464px; width: 244px; text-align: center; color: var(--green); font-weight: 300; font-size: 12px; line-height: 15.4px; }
  .copy p + p { margin-top: 15.4px; }
  .copy--info { top: 405px; }
  .copy--maker { top: 838px; color: var(--address); }

  .maker-mark { position: absolute; left: 519px; top: 930px; display: flex; align-items: center; gap: 5px; }
  .maker-mark__circle { width: 46px; height: 46px; border: 1px solid var(--green); border-radius: 50%; }
  .maker-mark__name { font-size: 8px; font-weight: 400; color: var(--green); }
</style>
</head>
<body>
<main class="canvas">
  <section class="panel panel--front" aria-label="Vorderseite"></section>
  <div class="spine" aria-hidden="true"></div>
  <section class="panel panel--back" aria-label="Rückseite"></section>

  <div class="brand-mark"><span class="brand-mark__name">Lindenkram</span></div>

  <p class="category">RÄUCHERSTÄBCHEN</p>

  <div class="band band--front">
    <div class="band__pattern" role="img" aria-label="Dreiecksmuster in Braun- und Taupetönen"></div>
    <h1 class="band__title"><span>WEIHRAUCH</span><span>AFRIKA</span></h1>
  </div>

  <p class="claim">NATUR PUR</p>

  <div class="count">10 St</div>
  <div class="lettering" role="img" aria-label="Handschriftzug: Made with love in Germany"></div>

  <div class="band band--back">
    <div class="band__pattern" role="img" aria-label="Dreiecksmuster in Braun- und Taupetönen"></div>
    <h2 class="band__title"><span>WEIHRAUCH</span><span>AFRIKA</span></h2>
  </div>

  <div class="copy copy--info">
    <p>Naturreine Räucherstäbchen<br>hergestellt mit den<br>reinsten Rohstoffen</p>
    <p>Ohne chemische oder<br>synthetische Zusätze,<br>kein Parfum,<br>keine Abbrennhilfe</p>
    <p>Brenndauer: ca. 45- 60min</p>
    <p>Eine Verpackung beinhaltet<br>10 Räucherstäbchen.</p>
  </div>

  <div class="copy copy--maker">
    <p>Hergestellt von:<br>Made by<br>Lindenkram<br>Birkenauer Weg 14<br>35127 Lindental</p>
  </div>

  <div class="maker-mark">
    <span class="maker-mark__circle"></span>
    <span class="maker-mark__name">lindenkram.de</span>
  </div>
</main>
</body>
</html>
```